Wordpress site needed for company's Healthcare Web App

Healthcare web app needs wordpress web design for web site that provides an overview of the product, a page explaining key features, a blog, a press release announcement section, customer testimonials, contact us, sign up page, invite friends.

The website should use the color scheme including in the logo. This web site is not the app, this website will be used to introduce the app.

Target Market(s)

Doctors, enterprise healthcare professionals, patients who will use patient portals to access their health info. (not the app itself, but this site introduces the app)

Industry/Entity Type

Health Care

Coding

Coded - Design and coding required

Number of Pages Required

5+ page

Font styles to use
Sans Serif

Requirements
Must have
• This is a Wordpress based site.
• Product Overview, Key Product Features, Blog, Press Releases, Events, Embedded Videos explaining the product and demo'ing features, Sign Up Page for people interested,
Nice to have
• Uplifting Hero Image for Healthcare Tech, color scheme fitting with logo

```html
<!DOCTYPE html>
<html lang="en">
<head>
<meta charset="utf-8">
<title>CareLedger — Personal Medical Records App</title>
<link rel="stylesheet" href="https://fonts.googleapis.com/css2?family=Lato:ital,wght@0,300;0,400;0,700;0,900;1,400;1,700&display=swap">
<style>
:root{
  --teal:#2a8ba8;
  --teal-dark:#1c7d99;
  --navy:#10243a;
  --paper:#f3f1e8;
  --paper-dark:#e6e4da;
  --ink:#4a4a4a;
  --ink-soft:#6a6a6a;
  --white:#ffffff;
  --line:#d6d3c6;
}
*{margin:0;padding:0;box-sizing:border-box}
html,body{width:1200px;height:3103px;overflow:hidden}
body{font-family:'Lato',sans-serif;background:var(--paper);color:var(--ink);position:relative}
.abs{position:absolute}

/* hero */
.hero{left:0;top:0;width:1200px;height:569px;background:linear-gradient(100deg,#0d2033 0%,#1c3d5c 45%,#3f6e90 75%,#23496a 100%)}
.hero-photo{right:0;top:0;width:620px;height:569px;background:radial-gradient(ellipse at 65% 45%,rgba(230,236,240,.55) 0%,rgba(120,160,190,.25) 35%,rgba(20,50,80,0) 70%)}
.nav-bar{left:0;top:0;width:1200px;height:86px;background:rgba(255,255,255,.08)}
.brand{left:161px;top:26px;display:flex;align-items:center;gap:10px;color:var(--white);font-weight:700;font-size:30px;line-height:34px}
.brand-mark{width:30px;height:30px;border-radius:50%;background:var(--white)}
.nav{left:496px;top:34px;display:flex;gap:18px;font-size:13px;line-height:16px;color:var(--white);font-weight:400}
.nav-btn{top:28px;height:27px;padding:0 12px;border:1px solid rgba(255,255,255,.75);border-radius:3px;color:var(--white);font-size:13px;line-height:25px}
.hero-title{left:163px;top:255px;color:var(--white);font-size:36px;line-height:37px;font-weight:300}
.hero-title b{font-weight:700}
.hero-cta{left:161px;top:451px;width:191px;height:48px;background:var(--teal);border:2px solid #6fc0d6;color:var(--white);font-size:17px;font-weight:700;text-align:center;line-height:44px;border-radius:3px}

/* section titles */
.sec-title{font-size:37px;font-weight:400;color:#6d6d6d;line-height:44px}
.sec-title span{color:var(--teal)}
.heart{width:22px;height:22px}

/* about */
.about-title{left:163px;top:636px}
.about-text{left:163px;top:716px;width:460px;font-size:11.5px;line-height:15.5px;color:var(--ink)}
.read-more{left:163px;top:855px;font-size:14px;color:var(--teal);text-decoration:underline}
.about-art{left:641px;top:621px;width:440px;height:320px;border-radius:14px;background:linear-gradient(135deg,#eaf2ef 0%,#cfe3da 45%,#9fc8cf 100%)}

/* features */
.features{left:0;top:972px;width:1200px;height:522px;background:var(--paper-dark)}
.phone-art{left:445px;top:1128px;width:310px;height:366px;border-radius:14px 14px 0 0;background:linear-gradient(180deg,#d9e2e0 0%,#c6d8d9 55%,#b9cfd2 100%)}
.feat{width:240px}
.feat h3{font-size:14px;font-weight:400;color:var(--teal);line-height:16px;margin-bottom:3px}
.feat p{font-size:11px;line-height:14px;color:var(--ink)}
.feat.left{text-align:right;left:108px}
.feat.right{left:834px}
.f-icon{width:46px;height:46px;background:var(--white);border:1px solid var(--line)}
.f-link{height:1px;background:#bfbcb0}

/* demo */
.demo-title{left:0;width:1200px;top:1528px;text-align:center}
.tablet{left:352px;top:1634px;width:507px;height:300px;border-radius:18px;background:#151515;padding:30px}
.tablet-screen{width:100%;height:100%;background:linear-gradient(135deg,#e4e7e8,#c9cfd2)}

/* testimonials */
.testi{left:0;top:2017px;width:1200px;height:404px;background:var(--paper-dark)}
.quote{left:203px;top:2150px;width:812px;font-size:11.5px;line-height:22px;font-style:italic;color:var(--ink);text-align:center}
.quote .qm{font-size:15px;font-style:normal;font-weight:900;color:#333}
.quote-author{left:0;width:1200px;top:2228px;text-align:center;font-size:13px;font-weight:700;font-style:italic;color:#333}
.avatar{left:569px;top:2270px;width:62px;height:68px;border:3px solid var(--white);background:linear-gradient(180deg,#6d88a4,#2c4560);box-shadow:0 0 0 1px var(--line)}
.dot{top:2356px;width:7px;height:7px;border-radius:50%;background:#9ab6c2}

/* blog and news */
.col-title{font-size:37px;font-weight:400;line-height:44px;color:#6d6d6d}
.col-title span{color:var(--teal)}
.col-rule{height:1px;background:var(--line)}
.blog-img{width:141px;height:108px;border:4px solid var(--white);box-shadow:0 0 0 1px var(--line)}
.date-tag{width:34px;height:24px;background:var(--teal);color:var(--white);font-size:10px;font-weight:700;line-height:11px;text-align:center;padding-top:1px}
.date-tag sup{font-size:6px;line-height:0}
.post h4{font-size:14px;font-weight:700;color:#333;margin-bottom:8px;line-height:17px}
.post p{font-size:10.5px;line-height:14px;color:var(--ink)}
.news-date{width:58px;height:62px;background:var(--white);border:1px solid var(--line);text-align:center}
.news-date .m{display:block;background:var(--teal-dark);color:var(--white);font-size:11px;font-weight:700;line-height:18px}
.news-date .d{display:block;font-size:25px;font-weight:700;color:#333;line-height:40px}
.news-rule{height:1px;background:var(--line);left:629px;width:410px}

/* signup */
.signup{left:0;top:2851px;width:1200px;height:201px;background:var(--teal-dark)}
.signup-title{left:0;width:1200px;top:2873px;text-align:center;font-size:26px;line-height:32px;font-weight:400;color:var(--white)}
.signup-sub{left:0;width:1200px;top:2914px;text-align:center;font-size:10px;font-style:italic;font-weight:700;color:var(--white)}
.field{top:2959px;height:35px;background:var(--white);font-size:10px;color:#999;line-height:35px;padding-left:14px;font-style:italic}
.submit{left:838px;top:2959px;width:108px;height:35px;background:#1c2730;color:var(--white);font-size:12px;font-weight:700;text-align:center;line-height:35px}

/* footer */
.footer-copy{left:163px;top:3072px;font-size:9.5px;color:#555}
.footer-brand{left:912px;top:3066px;font-size:18px;font-weight:700;color:var(--teal);display:flex;gap:6px;align-items:center}
.footer-brand i{width:14px;height:14px;background:var(--teal);border-radius:50%;display:block}
</style>
</head>
<body>

<!-- hero -->
<header class="abs hero"></header>
<div class="abs hero-photo" role="img" aria-label="Photo of a hand holding a smartphone showing the app, over a blurred medical technology background"></div>
<div class="abs nav-bar"></div>
<div class="abs brand"><span class="brand-mark"></span>CareLedger</div>
<nav class="abs nav"><span>Home</span><span>About Apps</span><span>Features</span><span>Blog</span><span>Press</span><span>Contact Us</span></nav>
<span class="abs nav-btn" style="left:900px">Sign Up</span>
<span class="abs nav-btn" style="left:975px">Log In</span>
<h1 class="abs hero-title">Comprehensive<br><b>Record-keeping App</b> For<br>Your <b>Personal Medical<br>Information.</b></h1>
<svg class="abs" style="left:360px;top:380px" width="60" height="70" viewBox="0 0 60 70"><path d="M50 5 C60 30 45 55 14 58" fill="none" stroke="#fff" stroke-width="3"/><path d="M22 48 L10 58 L24 64" fill="none" stroke="#fff" stroke-width="3"/></svg>
<a class="abs hero-cta">Download App Now</a>

<!-- about -->
<h2 class="abs sec-title about-title">About <span>Care Ledger</span></h2>
<svg class="abs heart" style="left:163px;top:686px" viewBox="0 0 22 22"><circle cx="11" cy="11" r="9" fill="none" stroke="#2a8ba8" stroke-width="1.5"/><path d="M11 15 L6.5 10.5 A2.4 2.4 0 0 1 11 7.8 A2.4 2.4 0 0 1 15.5 10.5 Z" fill="#2a8ba8"/></svg>
<p class="abs about-text">Lorem ipsum dolor sit amet, consectetuer adipiscing elit, sed diam nonummy nibh euismod tincidunt ut laoreet dolore magna aliquam erat volutpat. Ut wisi enim ad minim veniam, quis nostrud exerci tation ullamcorper suscipit lobortis nisl ut aliquip ex ea commodo consequat. Duis autem vel eum iriure dolor in hendrerit in vulputate velit esse molestie consequat, vel illum dolore eu feugiat nulla facilisis at vero eros et accumsan et iusto odio dignissim qui blandit praesent luptatum zzril delenit augue duis dolore te feugait nulla facilisi. Ut wisi enim ad minim veniam, quis nostrud exerci tation ullamcorper suscipit lobortis nisl ut aliquip ex ea commodo consequat.</p>
<a class="abs read-more">Read More</a>
<div class="abs about-art" role="img" aria-label="Illustration of a stethoscope, laptop, tablet, phone, medical chart and medicine bottle"></div>

<!-- features -->
<section class="abs features"></section>
<h2 class="abs sec-title" style="left:0;width:1200px;top:1012px;text-align:center">App <span>Features</span></h2>
<svg class="abs heart" style="left:589px;top:1062px" viewBox="0 0 22 22"><circle cx="11" cy="11" r="9" fill="none" stroke="#2a8ba8" stroke-width="1.5"/><path d="M11 15 L6.5 10.5 A2.4 2.4 0 0 1 11 7.8 A2.4 2.4 0 0 1 15.5 10.5 Z" fill="#2a8ba8"/></svg>
<div class="abs phone-art" role="img" aria-label="Illustration of a hand holding a phone with the app's health icons and a Download App Now button"></div>

<div class="abs feat left" style="top:1101px"><h3>It's for the whole family</h3><p>Lorem ipsum dolor sit amet,<br>consectetuer piscing .</p></div>
<div class="abs feat left" style="top:1197px"><h3>A medical record and more</h3><p>Lorem ipsum dolor sit amet,<br>consectetuer piscing .</p></div>
<div class="abs feat left" style="top:1294px"><h3>A digital file cabinet</h3><p>Lorem ipsum dolor sit amet,<br>consectetuer piscing .</p></div>
<div class="abs feat left" style="top:1389px"><h3>Chart test results with<br>sophistication</h3><p>Lorem ipsum dolor sit amet,<br>consectetuer piscing .</p></div>

<div class="abs feat right" style="top:1101px"><h3>21st century record-keeping</h3><p>Lorem ipsum dolor sit amet,<br>consectetuer piscing .</p></div>
<div class="abs feat right" style="top:1197px"><h3>Works with your calendar</h3><p>Lorem ipsum dolor sit amet,<br>consectetuer piscing .</p></div>
<div class="abs feat right" style="top:1294px"><h3>From blood tests to X-rays</h3><p>Lorem ipsum dolor sit amet,<br>consectetuer piscing .</p></div>
<div class="abs feat right" style="top:1396px"><h3>Have a long medical history</h3><p>Lorem ipsum dolor sit amet,<br>consectetuer piscing .</p></div>

<!-- feature icons -->
<svg class="abs f-icon" style="left:362px;top:1105px" viewBox="0 0 46 46"><circle cx="17" cy="18" r="5" fill="#2a8ba8"/><circle cx="29" cy="18" r="5" fill="#2a8ba8"/><rect x="10" y="25" width="26" height="10" rx="4" fill="#2a8ba8"/></svg>
<svg class="abs f-icon" style="left:362px;top:1201px" viewBox="0 0 46 46"><rect x="14" y="10" width="18" height="26" fill="none" stroke="#2a8ba8" stroke-width="2"/><path d="M18 18h10M18 23h10M18 28h7" stroke="#2a8ba8" stroke-width="2"/></svg>
<svg class="abs f-icon" style="left:362px;top:1298px" viewBox="0 0 46 46"><rect x="10" y="14" width="26" height="20" fill="#2a8ba8"/><path d="M23 19v10M18 24h10" stroke="#fff" stroke-width="2.5"/></svg>
<svg class="abs f-icon" style="left:362px;top:1395px" viewBox="0 0 46 46"><path d="M13 34V24M19 34V16M25 34V20M31 34V12" stroke="#2a8ba8" stroke-width="3"/></svg>
<svg class="abs f-icon" style="left:776px;top:1105px" viewBox="0 0 46 46"><rect x="14" y="10" width="18" height="26" fill="#2a8ba8"/><path d="M17 17h12M17 23h12M17 29h12" stroke="#fff" stroke-width="2"/></svg>
<svg class="abs f-icon" style="left:776px;top:1201px" viewBox="0 0 46 46"><rect x="11" y="13" width="24" height="22" fill="none" stroke="#2a8ba8" stroke-width="2"/><path d="M11 19h24M16 24h3M22 24h3M28 24h3M16 29h3M22 29h3" stroke="#2a8ba8" stroke-width="2"/></svg>
<svg class="abs f-icon" style="left:776px;top:1298px" viewBox="0 0 46 46"><path d="M14 32L30 16M26 12l8 8M12 34l4-4" stroke="#2a8ba8" stroke-width="3"/></svg>
<svg class="abs f-icon" style="left:776px;top:1395px" viewBox="0 0 46 46"><rect x="15" y="10" width="16" height="26" rx="2" fill="#2a8ba8"/><path d="M18 17h10M18 22h10M18 27h10" stroke="#fff" stroke-width="2"/></svg>

<div class="abs f-link" style="left:408px;top:1128px;width:60px"></div>
<div class="abs f-link" style="left:408px;top:1224px;width:37px"></div>
<div class="abs f-link" style="left:408px;top:1321px;width:37px"></div>
<div class="abs f-link" style="left:408px;top:1418px;width:37px"></div>
<div class="abs f-link" style="left:732px;top:1128px;width:44px"></div>
<div class="abs f-link" style="left:755px;top:1224px;width:21px"></div>
<div class="abs f-link" style="left:755px;top:1321px;width:21px"></div>
<div class="abs f-link" style="left:755px;top:1418px;width:21px"></div>

<!-- demo -->
<h2 class="abs sec-title demo-title">App <span>Demonstration</span></h2>
<svg class="abs heart" style="left:589px;top:1578px" viewBox="0 0 22 22"><circle cx="11" cy="11" r="9" fill="none" stroke="#2a8ba8" stroke-width="1.5"/><path d="M11 15 L6.5 10.5 A2.4 2.4 0 0 1 11 7.8 A2.4 2.4 0 0 1 15.5 10.5 Z" fill="#2a8ba8"/></svg>
<div class="abs tablet"><div class="tablet-screen" role="img" aria-label="Embedded video showing a demonstration of the app"></div></div>

<!-- testimonials -->
<section class="abs testi"></section>
<h2 class="abs sec-title" style="left:0;width:1200px;top:2047px;text-align:center">User <span>Testimonials</span></h2>
<svg class="abs heart" style="left:589px;top:2097px" viewBox="0 0 22 22"><circle cx="11" cy="11" r="9" fill="none" stroke="#2a8ba8" stroke-width="1.5"/><path d="M11 15 L6.5 10.5 A2.4 2.4 0 0 1 11 7.8 A2.4 2.4 0 0 1 15.5 10.5 Z" fill="#2a8ba8"/></svg>
<p class="abs quote"><span class="qm">&ldquo;</span> Lorem ipsum dolor sit amet, consectetur adipiscing elit, sed do eiusmod tempor incididunt ut labore et dolore magna aliqua. Ut enim veniam, quis nostrud exercitation ullamco laboris nisi ut aliquip ex ea commodo consequat. Duis aute irure dolor in reprehenderit in voluptate velit esse cillum dolore eu fugiat nulla pariatur. Excepteur sint occaecat cupidatat non proident, sunt in culpa qui officia . <span class="qm">&rdquo;</span></p>
<p class="abs quote-author">- Sconsectetur adipiscing</p>
<div class="abs avatar" role="img" aria-label="Portrait photo of the reviewer"></div>
<span class="abs dot" style="left:585px;background:var(--teal)"></span>
<span class="abs dot" style="left:597px"></span>
<span class="abs dot" style="left:609px"></span>

<!-- blog -->
<h2 class="abs col-title" style="left:165px;top:2456px">Latest <span>Blog</span></h2>
<svg class="abs heart" style="left:165px;top:2506px" viewBox="0 0 22 22"><circle cx="11" cy="11" r="9" fill="none" stroke="#2a8ba8" stroke-width="1.5"/><path d="M11 15 L6.5 10.5 A2.4 2.4 0 0 1 11 7.8 A2.4 2.4 0 0 1 15.5 10.5 Z" fill="#2a8ba8"/></svg>
<div class="abs col-rule" style="left:192px;top:2517px;width:385px"></div>

<div class="abs blog-img" style="left:165px;top:2551px;background:linear-gradient(135deg,#1d3c5e,#5d87aa)" role="img" aria-label="Blog photo of a digital healthcare interface"></div>
<div class="abs date-tag" style="left:331px;top:2551px">27<sup>th</sup><br>Oct</div>
<div class="abs post" style="left:372px;top:2553px;width:210px"><h4>Lorem ipsum dolor sit amet,</h4></div>
<div class="abs post" style="left:331px;top:2584px;width:250px"><p>Fusce elementum, nulla vel pellentes consequat, ante nulla hendrerit arcu, ac tincidunt mauris lacus sed leo. vamus suscipit molestie vestibulum. Lorem ipsum dolor sit amet.</p></div>

<div class="abs blog-img" style="left:165px;top:2690px;background:linear-gradient(135deg,#274a66,#c68a55)" role="img" aria-label="Blog photo of a hand with glowing medical icons"></div>
<div class="abs date-tag" style="left:331px;top:2690px">25<sup>th</sup><br>Oct</div>
<div class="abs post" style="left:372px;top:2692px;width:210px"><h4>Lorem ipsum dolor sit amet,</h4></div>
<div class="abs post" style="left:331px;top:2723px;width:250px"><p>Fusce elementum, nulla vel pellentes consequat, ante nulla hendrerit arcu, ac tincidunt mauris lacus sed leo. vamus suscipit molestie vestibulum. Lorem ipsum dolor sit amet.</p></div>

<!-- news -->
<h2 class="abs col-title" style="left:627px;top:2456px">News &amp; <span>Events</span></h2>
<svg class="abs heart" style="left:627px;top:2506px" viewBox="0 0 22 22"><circle cx="11" cy="11" r="9" fill="none" stroke="#2a8ba8" stroke-width="1.5"/><path d="M11 15 L6.5 10.5 A2.4 2.4 0 0 1 11 7.8 A2.4 2.4 0 0 1 15.5 10.5 Z" fill="#2a8ba8"/></svg>
<div class="abs col-rule" style="left:654px;top:2517px;width:385px"></div>

<div class="abs news-date" style="left:629px;top:2549px"><span class="m">Nov</span><span class="d">14</span></div>
<div class="abs post" style="left:699px;top:2549px;width:340px"><h4 style="margin-bottom:4px">Lorem ipsum dolor sit amet,</h4><p>Fusce elementum, nulla vel pellentes consequat, ante nulla hendrerit arcu, ac tincidunt mauris lacus sed leo. vamus suscipit molestie vestibulum. Lorem ipsum dolor sit amet. <span style="color:var(--teal)">[+]</span></p></div>
<div class="abs news-rule" style="top:2627px"></div>

<div class="abs news-date" style="left:629px;top:2640px"><span class="m">Nov</span><span class="d">12</span></div>
<div class="abs post" style="left:699px;top:2640px;width:340px"><h4 style="margin-bottom:4px">Lorem ipsum dolor sit amet,</h4><p>Fusce elementum, nulla vel pellentes consequat, ante nulla hendrerit arcu, ac tincidunt mauris lacus sed leo. vamus suscipit molestie vestibulum. Lorem ipsum dolor sit amet. <span style="color:var(--teal)">[+]</span></p></div>
<div class="abs news-rule" style="top:2716px"></div>

<div class="abs news-date" style="left:629px;top:2727px"><span class="m">Nov</span><span class="d">10</span></div>
<div class="abs post" style="left:699px;top:2727px;width:340px"><h4 style="margin-bottom:4px">Lorem ipsum dolor sit amet,</h4><p>Fusce elementum, nulla vel pellentes consequat, ante nulla hendrerit arcu, ac tincidunt mauris lacus sed leo. vamus suscipit molestie vestibulum. Lorem ipsum dolor sit amet. <span style="color:var(--teal)">[+]</span></p></div>
<div class="abs news-rule" style="top:2804px"></div>

<!-- signup -->
<section class="abs signup"></section>
<h2 class="abs signup-title">Join our email list</h2>
<p class="abs signup-sub">Lorem ipsum dolor sit amet, consectetuer adipiscing elit, sed diam nonummy nibh euismod tincidunt ut laoreet</p>
<div class="abs field" style="left:304px;width:259px"></div>
<div class="abs field" style="left:571px;width:259px">
  <svg width="10" height="11" viewBox="0 0 10 11" style="vertical-align:-1px;margin-right:6px"><rect x="1" y="5" width="8" height="6" fill="#999"/><path d="M3 5V3a2 2 0 0 1 4 0v2" fill="none" stroke="#999" stroke-width="1.3"/></svg>Password</div>
<div class="abs submit">SUBMIT</div>

<!-- footer -->
<p class="abs footer-copy">Copyright© 2016 Care Ledger. All rights reserved</p>
<div class="abs footer-brand"><i></i>CareLedger</div>

</body>
</html>
```